WordPress Website Design Project

Technical & Functional Deliverables
WordPress CMS
Fully responsive design
Integrated WhatsApp chatbot
Custom article filtering system
SEO-friendly site structure & performance optimization
CMS user manual & training session
Updates

Need extra days to review

Industry/Entity Type

Industrial Safety and Compliance

Coding

Coded - Design and coding required

Number of Pages Required

5+ page

Font styles to use
Sans Serif

Colors
0054AA
0677BA
7BADD7
CADEEF
E8F1F8

```html
<!DOCTYPE html>
<html lang="en">
<head>
<meta charset="utf-8">
<title>Bastion — Industrial Safety & Compliance</title>
<link href="https://fonts.googleapis.com/css2?family=Inter:wght@400;500;600;700&display=swap" rel="stylesheet">
<style>
:root{
  --blue-deep:#0054AA;
  --blue:#0677BA;
  --blue-soft:#7BADD7;
  --blue-pale:#CADEEF;
  --blue-mist:#E8F1F8;
  --ink:#111418;
  --text:#2b2f36;
  --muted:#5d6470;
  --night:#0b0f16;
  --white:#ffffff;
}
*{margin:0;padding:0;box-sizing:border-box}
html,body{width:1200px;height:3816px;overflow:hidden}
body{font-family:'Inter',sans-serif;color:var(--text);background:var(--white);position:relative}
.section-title{position:absolute;left:0;width:1200px;text-align:center;font-size:30px;font-weight:600;color:var(--ink);letter-spacing:0.5px}
.photo{position:absolute}

/* hero */
.hero{position:absolute;left:0;top:0;width:1200px;height:640px;background:linear-gradient(135deg,#0d131c 0%,#05080d 100%)}
.brand{position:absolute;font-weight:700;color:var(--white);letter-spacing:3px}
.nav{position:absolute;right:72px;top:30px;display:flex;font-size:14px;color:#e6e9ee}
.nav span{padding:0 14px;border-left:1px solid #8a93a0;line-height:14px}
.nav span:first-child{border-left:none}
.hero h1{position:absolute;left:72px;top:212px;width:540px;font-size:40px;line-height:54px;font-weight:600;color:var(--white);white-space:nowrap}
.btn{position:absolute;left:78px;top:380px;width:164px;height:48px;background:var(--blue-soft);color:var(--white);font-size:14px;font-weight:500;display:flex;align-items:center;justify-content:center;gap:8px}

/* values */
.values-tag{position:absolute;left:636px;top:782px;color:var(--blue);font-size:20px}
.values h2{position:absolute;left:636px;top:820px;width:500px;font-size:38px;line-height:46px;font-weight:600;color:var(--ink)}
.values-body{position:absolute;left:636px;top:930px;width:490px;font-size:13.5px;line-height:20px;color:var(--text)}
.values-body p{margin-bottom:13px}
.values-body b{color:var(--ink)}

/* work */
.band{position:absolute;left:0;width:1200px;background:var(--blue-mist)}
.arrow{position:absolute;width:30px;height:30px;border-radius:50%;background:var(--white);display:flex;align-items:center;justify-content:center;box-shadow:0 1px 4px rgba(0,0,0,.25)}

/* clients */
.client{position:absolute;width:176px;text-align:center;font-size:22px;font-weight:700;color:var(--blue-deep);display:flex;align-items:center;justify-content:center;gap:8px;white-space:nowrap}
.client i{display:inline-block;width:14px;height:14px;border-radius:50%;background:var(--blue)}

/* solutions */
.card{position:absolute;top:2595px;width:248px;height:182px;background:var(--white);border-bottom:4px solid var(--blue)}
.card .icon{position:absolute;left:26px;top:26px;width:64px;height:64px;border-radius:50%;background:#12223a;display:flex;align-items:center;justify-content:center}
.card p{position:absolute;left:26px;top:106px;width:180px;font-size:15px;line-height:20px;color:var(--ink)}

/* people */
.person-name{position:absolute;top:3362px;font-size:19px;color:var(--ink);white-space:nowrap}
.person-role{position:absolute;top:3392px;font-size:12px;color:var(--muted);white-space:nowrap}

/* footer */
.footer{position:absolute;left:0;top:3512px;width:1200px;height:304px;background:linear-gradient(135deg,#0d131c,#05080d);color:var(--white)}
.footer .tag{position:absolute;left:72px;top:44px;width:330px;font-size:17px;line-height:28px}
.footer .links{position:absolute;right:72px;top:64px;display:flex;gap:18px;font-size:14px;color:#dfe3ea}
.footer .legal{position:absolute;left:72px;top:202px;font-size:13px;color:#dfe3ea}
.footer .copy{position:absolute;right:72px;top:246px;font-size:12px;color:#dfe3ea}
.footer .social{position:absolute;left:72px;top:240px;width:30px;height:30px;border:1.5px solid #dfe3ea;border-radius:50%}
</style>
</head>
<body>

<!-- Hero -->
<header class="hero">
  <div class="brand" style="left:72px;top:18px;font-size:30px">BASTION</div>
  <nav class="nav"><span>About us</span><span>Solutions</span><span>Contact us</span><span>Articles</span></nav>
  <h1>Your Partner In Industrial<br>Safety &amp; Compliance</h1>
  <div class="btn">
    <svg width="14" height="12" viewBox="0 0 14 12"><rect x="0.75" y="0.75" width="12.5" height="10.5" fill="none" stroke="#fff" stroke-width="1.5"/><path d="M1 1 L7 7 L13 1" fill="none" stroke="#fff" stroke-width="1.5"/></svg>
    CONTACT US
  </div>
  <div class="photo" role="img" aria-label="Photo of a business team meeting around a laptop in a bright office" style="left:632px;top:108px;width:496px;height:348px;background:linear-gradient(135deg,#c9d3dc,#8a98a6 60%,#4c5865)"></div>
</header>

<!-- Values -->
<section class="values">
  <div class="section-title" style="top:700px">OUR VALUES</div>
  <div class="photo" role="img" aria-label="Photo of three professionals in business attire walking together" style="left:72px;top:790px;width:502px;height:510px;background:linear-gradient(160deg,#e7ebef,#b6bfc8 55%,#3b434f)"></div>
  <div class="values-tag">| We are Bastion |</div>
  <h2>Your Partner in Industrial Safety and Compliance</h2>
  <div class="values-body">
    <p>Mission Statement and Core Values</p>
    <p>To provide expert guidance and practical solutions in industrial safety and compliance, delivering clarity, reliability, and peace of mind to every partner we serve.</p>
    <p>We achieve this mission by staying true to our foundational values:</p>
    <p><b>Assurance:</b> Providing confidence through technically robust solutions.</p>
    <p><b>Reliability:</b> Ensuring consistent performance in demanding situations.</p>
    <p><b>Commitment:</b> Fulfilling promises and exceeding expectations.</p>
    <p><b>Honor:</b> Upholding the highest ethical standards.</p>
    <p><b>Expertise:</b> Leveraging deep industry knowledge to solve complex challenges.</p>
    <p><b>Responsibility:</b> Taking full accountability from concept through completion.</p>
  </div>
</section>

<!-- Work -->
<section>
  <div class="band" style="top:1390px;height:600px"></div>
  <div class="section-title" style="top:1438px">OUR WORK</div>
  <div class="photo" role="img" aria-label="Photo of an industrial plant with stacked coins in warm light" style="left:72px;top:1530px;width:366px;height:380px;background:linear-gradient(160deg,#d9c7a8,#8fa3ad 55%,#4e6470)"></div>
  <div class="photo" role="img" aria-label="Photo of an aircraft jet engine on the apron at sunset" style="left:452px;top:1530px;width:294px;height:380px;background:linear-gradient(170deg,#e3a86a,#9aa8b3 55%,#48525c)"></div>
  <div class="photo" role="img" aria-label="Photo of robotic arms on an automotive assembly line" style="left:760px;top:1530px;width:368px;height:380px;background:linear-gradient(160deg,#c9a46a,#8a7760 50%,#3f3a35)"></div>
  <div class="arrow" style="left:57px;top:1705px"><svg width="10" height="12" viewBox="0 0 10 12"><path d="M7 1 L2 6 L7 11" fill="none" stroke="#111" stroke-width="2"/></svg></div>
  <div class="arrow" style="left:1113px;top:1705px"><svg width="10" height="12" viewBox="0 0 10 12"><path d="M3 1 L8 6 L3 11" fill="none" stroke="#111" stroke-width="2"/></svg></div>
</section>

<!-- Clients -->
<section>
  <div class="section-title" style="top:2058px">OUR CLIENTS</div>
  <div class="client" style="left:72px;top:2190px">Northrise</div>
  <div class="client" style="left:248px;top:2190px"><i></i>Corvane</div>
  <div class="client" style="left:424px;top:2190px">Tellara</div>
  <div class="client" style="left:600px;top:2190px"><i></i>Orvik</div>
  <div class="client" style="left:776px;top:2190px">Marlow Chem</div>
  <div class="client" style="left:952px;top:2190px"><i></i>Skyline Air</div>
  <div class="client" style="left:72px;top:2296px"><i></i>Harbex</div>
  <div class="client" style="left:248px;top:2296px">Solvane</div>
  <div class="client" style="left:424px;top:2296px">Keystrand</div>
  <div class="client" style="left:600px;top:2296px"><i></i>Halvern</div>
  <div class="client" style="left:776px;top:2296px">Petrolux</div>
  <div class="client" style="left:952px;top:2296px">Quayport</div>
</section>

<!-- Solutions -->
<section>
  <div class="band" style="top:2455px;height:400px"></div>
  <div class="section-title" style="top:2512px">OUR SOLUTIONS</div>
  <div class="card" style="left:72px">
    <div class="icon"><svg width="30" height="30" viewBox="0 0 30 30"><circle cx="15" cy="15" r="6" fill="none" stroke="#fff" stroke-width="2"/><path d="M15 3v5M15 22v5M3 15h5M22 15h5M6.5 6.5l3.5 3.5M20 20l3.5 3.5M6.5 23.5l3.5-3.5M20 10l3.5-3.5" stroke="#fff" stroke-width="2"/></svg></div>
    <p>Engineering &amp; design</p>
  </div>
  <div class="card" style="left:341px">
    <div class="icon"><svg width="30" height="30" viewBox="0 0 30 30"><circle cx="15" cy="10" r="5" fill="none" stroke="#fff" stroke-width="2"/><path d="M5 27c1-6 5-9 10-9s9 3 10 9" fill="none" stroke="#fff" stroke-width="2"/></svg></div>
    <p>Technical Support &amp;<br>Site Services</p>
  </div>
  <div class="card" style="left:610px">
    <div class="icon"><svg width="30" height="30" viewBox="0 0 30 30"><rect x="7" y="4" width="16" height="22" fill="none" stroke="#fff" stroke-width="2"/><path d="M11 11l2 2 4-4M11 19h8" fill="none" stroke="#fff" stroke-width="2"/></svg></div>
    <p>Risk Management &amp;<br>Compliance Services</p>
  </div>
  <div class="card" style="left:880px">
    <div class="icon"><svg width="30" height="30" viewBox="0 0 30 30"><path d="M4 19a11 11 0 0 1 22 0M4 19l3-3M26 19l-3-3M15 24V12" fill="none" stroke="#fff" stroke-width="2"/></svg></div>
    <p>Transitioning to<br>Fluorine-Free Foam</p>
  </div>
</section>

<!-- People -->
<section>
  <div class="section-title" style="top:2912px">OUR PEOPLE</div>
  <div class="photo" role="img" aria-label="Portrait of the project manager" style="left:72px;top:3012px;width:204px;height:332px;background:linear-gradient(180deg,#eef0f2,#b9c6d3)"></div>
  <div class="photo" role="img" aria-label="Portrait of the mechanical engineer" style="left:285px;top:3012px;width:204px;height:332px;background:linear-gradient(180deg,#f1eeec,#d9a89a)"></div>
  <div class="photo" role="img" aria-label="Portrait of the sustainability consultant" style="left:498px;top:3012px;width:204px;height:332px;background:linear-gradient(180deg,#e6e9ec,#3e4d66)"></div>
  <div class="photo" role="img" aria-label="Portrait of the resilience engineer" style="left:711px;top:3012px;width:204px;height:332px;background:linear-gradient(180deg,#eef0f3,#a9bfd8)"></div>
  <div class="photo" role="img" aria-label="Portrait of the structural engineer" style="left:924px;top:3012px;width:204px;height:332px;background:linear-gradient(180deg,#d7d2cc,#3b4656)"></div>
  <div class="person-name" style="left:72px">Daniel Reyes</div><div class="person-role" style="left:72px">Project Manager</div>
  <div class="person-name" style="left:285px">Maya Lindqvist</div><div class="person-role" style="left:285px">Mechanical Engineer</div>
  <div class="person-name" style="left:498px">Lior Adams</div><div class="person-role" style="left:498px">Sustainability Consultant</div>
  <div class="person-name" style="left:711px">Chloe Barnett</div><div class="person-role" style="left:711px">Resilience Engineer</div>
  <div class="person-name" style="left:924px">Samuel Hart</div><div class="person-role" style="left:924px">Structural Engineer</div>
</section>

<!-- Footer -->
<footer class="footer">
  <div class="tag">We Are Bastion. Your Partner In<br>Industrial Safety And Compliance</div>
  <div class="links"><span>Home</span><span>About Us</span><span>Solutions</span><span>Articles</span><span>Contact Us</span></div>
  <div class="brand" style="right:72px;top:194px;font-size:30px">BASTION</div>
  <div class="legal">Legal &nbsp;|&nbsp; Cookies &nbsp;|&nbsp; Privacy</div>
  <div class="social" aria-label="Social profile link"></div>
  <div class="copy">©Bastion (S) Pte Ltd 2025</div>
</footer>

</body>
</html>
```